A5 Flyer for Financial Services Business

I am after a re-design of our business flyer to fit in with our new branding style and logo colour scheme. Wanting something with a bit of designer flair that I could not create myself. I have included the flyer which I created which lacks style so dazzle me.

I want to use the same content.

Text for main body of flyer is

Are you a small business owner, tradie or PAVC Service Provider struggling to stay on top of your bookkeeping and compliance obligations? If so we would love to help you get back on track and take control of your business finances so that you can make informed business decisions and focus on what you do best.

We have over 20 years industry experience and, as a small business ourselves, we are able to offer our clients a personal bookkeeping solution tailored to meet the needs of your business.

Accounts Payable | Accounts Receivable
Customer Invoicing
Bank and Credit Card Reconciliations
Payroll | Superannuation | Payroll Tax
Business Activity | Instalment Activity Statements
Regular Financial Reports
Ledgerly and Tallybook Set-Up and Training

```html
<!DOCTYPE html>
<html lang="en">
<head>
<meta charset="utf-8">
<title>Even Keel Ledger Services – Flyer</title>
<link href="https://fonts.googleapis.com/css2?family=Montserrat:wght@400;500;600;700&family=Roboto+Condensed:wght@400&display=swap" rel="stylesheet">
<style>
  :root{
    --teal:#10a39b;
    --teal-deep:#0b6f78;
    --navy:#0f2a3d;
    --body-bg:#ececec;
    --ink:#26323d;
    --slate:#4a5560;
    --white:#ffffff;
    --stage:#a9a9a9;
  }
  *{margin:0;padding:0;box-sizing:border-box}
  html,body{width:1200px;height:2372px;overflow:hidden}
  body{background:var(--stage);font-family:"Montserrat",sans-serif;position:relative}
  .flyer{position:absolute;left:53px;top:412px;width:1094px;height:1548px;background:var(--white);overflow:hidden;box-shadow:0 6px 18px rgba(0,0,0,.35)}
  .hero-art{position:absolute;left:0;top:0;width:1094px;height:720px}
  .brand{position:absolute;left:40px;top:60px;width:420px;text-align:center;color:var(--teal-deep)}
  .brand-dot{width:110px;height:110px;border-radius:50%;background:var(--teal-deep);margin:0 auto 22px}
  .brand-name{font-weight:500;font-size:38px;line-height:1.15;letter-spacing:1px}
  .headline{position:absolute;left:46px;top:370px;color:var(--white);font-weight:700;font-size:61px;line-height:70px}
  .intro{position:absolute;left:0;top:700px;width:1094px;height:303px;background:var(--body-bg);padding:28px 50px 0}
  .intro p{font-weight:500;font-size:22px;line-height:29px;color:var(--ink);margin-bottom:28px}
  .services{position:absolute;left:0;top:1003px;width:1094px;height:372px;background:var(--navy);border-top:8px solid var(--teal)}
  .service-list{list-style:none;position:absolute;left:40px;top:34px}
  .service-list li{display:flex;align-items:center;height:44px;color:var(--white);font-weight:500;font-size:22.5px}
  .service-list svg{width:28px;height:28px;margin-right:20px}
  .badge{position:absolute;left:824px;top:68px;width:190px;text-align:center}
  .badge-seal{width:188px;height:188px}
  .badge-text{font-family:"Roboto Condensed",sans-serif;color:#b8c2cb;font-size:20px;line-height:27px;margin-top:8px}
  .contact{position:absolute;left:0;top:1383px;width:1094px;height:165px;background:var(--teal);border-top:6px solid var(--white)}
  .contact-label{position:absolute;left:42px;top:32px;background:var(--white);color:var(--navy);font-weight:600;font-size:19px;padding:6px 14px;border-radius:10px;letter-spacing:.3px}
  .contact-phone{position:absolute;left:42px;top:86px;display:flex;align-items:center;color:var(--white);font-weight:600;font-size:36px}
  .contact-phone svg{width:34px;height:34px;margin-right:14px}
  .divider{position:absolute;left:375px;top:40px;width:2px;height:84px;background:var(--white)}
  .links{position:absolute;left:408px;top:30px}
  .links div{display:flex;align-items:center;height:52px;color:var(--white);font-weight:600;font-size:23px}
  .links svg{width:26px;height:26px;margin-right:22px}
</style>
</head>
<body>
<main class="flyer">
  <svg class="hero-art" viewBox="0 0 1094 720">
    <defs>
      <linearGradient id="photoTone" x1="0" y1="0" x2="1" y2="1">
        <stop offset="0" stop-color="#e9eef0"/>
        <stop offset=".55" stop-color="#d4d9dc"/>
        <stop offset="1" stop-color="#f2f2f2"/>
      </linearGradient>
      <linearGradient id="bandTone" x1="0" y1="0" x2="1" y2="0">
        <stop offset="0" stop-color="#10a39b"/>
        <stop offset="1" stop-color="#0b6f78"/>
      </linearGradient>
    </defs>
    <rect x="0" y="0" width="1094" height="720" fill="#ffffff"/>
    <polygon points="0,690 811,590 1094,700 1094,720 0,720" fill="#ececec"/>
    <polygon points="456,0 1094,0 1094,700 811,590 526,268" fill="url(#photoTone)" role="img" aria-label="Photo of a desk with a laptop, calculator and a hand writing on tax forms"/>
    <line x1="0" y1="320" x2="526" y2="254" stroke="#10a39b" stroke-width="4"/>
    <polygon points="0,333 526,265 811,586 0,683" fill="url(#bandTone)"/>
    <line x1="0" y1="698" x2="811" y2="600" stroke="#10a39b" stroke-width="4"/>
  </svg>

  <div class="brand">
    <div class="brand-dot"></div>
    <div class="brand-name">EVEN KEEL<br>LEDGER SERVICES</div>
  </div>

  <h1 class="headline">Bookkeeping<br>tailored to your<br>business needs</h1>

  <section class="intro">
    <p>Are you a small business owner, tradie or PAVC Service Provider struggling to stay on top of your bookkeeping and compliance obligations? If so we would love to help you get back on track and take control of your business finances so that you can make informed business decisions and focus on what you do best.</p>
    <p>We have over 20 years industry experience and, as a small business ourselves, we are able to offer our clients a personal bookkeeping solution tailored to meet the needs of your business.</p>
  </section>

  <section class="services">
    <ul class="service-list">
      <li><svg viewBox="0 0 28 28"><circle cx="13" cy="15" r="10" fill="none" stroke="#10a39b" stroke-width="2.5"/><path d="M8 14l5 5 12-14" fill="none" stroke="#10a39b" stroke-width="3.5"/></svg>Accounts Payable | Accounts Receivable</li>
      <li><svg viewBox="0 0 28 28"><circle cx="13" cy="15" r="10" fill="none" stroke="#10a39b" stroke-width="2.5"/><path d="M8 14l5 5 12-14" fill="none" stroke="#10a39b" stroke-width="3.5"/></svg>Customer Invoicing</li>
      <li><svg viewBox="0 0 28 28"><circle cx="13" cy="15" r="10" fill="none" stroke="#10a39b" stroke-width="2.5"/><path d="M8 14l5 5 12-14" fill="none" stroke="#10a39b" stroke-width="3.5"/></svg>Bank and Credit Card Reconciliations</li>
      <li><svg viewBox="0 0 28 28"><circle cx="13" cy="15" r="10" fill="none" stroke="#10a39b" stroke-width="2.5"/><path d="M8 14l5 5 12-14" fill="none" stroke="#10a39b" stroke-width="3.5"/></svg>Payroll | Superannuation | Payroll Tax</li>
      <li><svg viewBox="0 0 28 28"><circle cx="13" cy="15" r="10" fill="none" stroke="#10a39b" stroke-width="2.5"/><path d="M8 14l5 5 12-14" fill="none" stroke="#10a39b" stroke-width="3.5"/></svg>Business Activity | Instalment Activity Statements</li>
      <li><svg viewBox="0 0 28 28"><circle cx="13" cy="15" r="10" fill="none" stroke="#10a39b" stroke-width="2.5"/><path d="M8 14l5 5 12-14" fill="none" stroke="#10a39b" stroke-width="3.5"/></svg>Regular Financial Reports</li>
      <li><svg viewBox="0 0 28 28"><circle cx="13" cy="15" r="10" fill="none" stroke="#10a39b" stroke-width="2.5"/><path d="M8 14l5 5 12-14" fill="none" stroke="#10a39b" stroke-width="3.5"/></svg>Ledgerly and Tallybook Set-Up and Training</li>
    </ul>
    <div class="badge">
      <svg class="badge-seal" viewBox="0 0 188 188" role="img" aria-label="Registration badge">
        <circle cx="94" cy="94" r="90" fill="none" stroke="#c9d1d8" stroke-width="3"/>
        <circle cx="94" cy="94" r="58" fill="none" stroke="#c9d1d8" stroke-width="2"/>
      </svg>
      <div class="badge-text">BAS agent<br>41872306</div>
    </div>
  </section>

  <footer class="contact">
    <div class="contact-label">CONTACT INFORMATION</div>
    <div class="contact-phone">
      <svg viewBox="0 0 24 24"><path d="M6.6 10.8c1.4 2.8 3.8 5.1 6.6 6.6l2.2-2.2c.3-.3.7-.4 1-.2 1.1.4 2.3.6 3.6.6.6 0 1 .4 1 1V20c0 .6-.4 1-1 1C10.6 21 3 13.4 3 4c0-.6.4-1 1-1h3.5c.6 0 1 .4 1 1 0 1.3.2 2.5.6 3.6.1.3 0 .7-.2 1z" fill="none" stroke="#fff" stroke-width="2"/></svg>
      1300 482 615
    </div>
    <div class="divider"></div>
    <div class="links">
      <div><svg viewBox="0 0 24 24"><circle cx="12" cy="12" r="10" fill="none" stroke="#fff" stroke-width="1.8"/><ellipse cx="12" cy="12" rx="4.5" ry="10" fill="none" stroke="#fff" stroke-width="1.5"/><path d="M2 12h20M4 7h16M4 17h16" stroke="#fff" stroke-width="1.5"/></svg>www.evenkeelledgerservices.com.au</div>
      <div><svg viewBox="0 0 24 24"><rect x="2" y="5" width="20" height="14" rx="1.5" fill="#fff"/><path d="M2.5 6l9.5 7 9.5-7" fill="none" stroke="#10a39b" stroke-width="1.8"/></svg>www.evenkeelledgerservices.com.au</div>
    </div>
  </footer>
</main>
</body>
</html>
```